A label for my commercially sold local honey. This is a LABEL not a logo

3 inches high
2 inches wide

Target Market(s)

Customers who like "local" honey

Logo Text

Wildflower Honey -- 100% Pure & Unfiltered -- Florida

Logo styles of interest
Wordmark Logo
Requirements
Must have
• Wildflower Honey -- 100% Pure & Unfiltered -- Florida

Florida should be dominant

3 inches high / 2 inches wide

```html
<!DOCTYPE html>
<html lang="en">
<head>
<meta charset="utf-8">
<title>Wildflower Honey Label</title>
<link href="https://fonts.googleapis.com/css2?family=Smokum&family=Archivo:wght@800&family=Oswald:wght@600&display=swap" rel="stylesheet">
<style>
  :root {
    --backdrop: #585858;
    --label-yellow: #fbe07d;
    --ink: #141210;
    --gold-dark: #6b3a10;
    --gold-mid: #c98a2a;
    --gold-light: #fff1b0;
    --map-fill: #e9b93a;
    --map-edge: #b7811c;
  }
  html, body {
    margin: 0;
    padding: 0;
    width: 1200px;
    height: 1118px;
    overflow: hidden;
    background: var(--backdrop);
  }
  .label {
    position: absolute;
    left: 335px;
    top: 39px;
    width: 530px;
    height: 1040px;
    background: var(--label-yellow);
    overflow: hidden;
    color: var(--ink);
  }
  .label p, .label h1 { margin: 0; }
  .foil-band {
    position: absolute;
    left: 0;
    width: 100%;
    height: 30px;
    background: linear-gradient(90deg, var(--gold-dark) 0%, var(--gold-mid) 12%, var(--gold-light) 24%, var(--gold-mid) 36%, var(--gold-dark) 50%, var(--gold-mid) 64%, var(--gold-light) 78%, var(--gold-mid) 90%, var(--gold-dark) 100%);
  }
  .foil-band--top { top: 0; }
  .foil-band--bottom { bottom: 0; }
  .foil-band::after {
    content: "";
    position: absolute;
    left: 0; right: 0; top: 40%;
    height: 20%;
    background: rgba(255, 248, 210, 0.35);
  }
  .title-word {
    position: absolute;
    left: 0;
    width: 100%;
    text-align: center;
    font-family: "Smokum", "Rye", serif;
    font-weight: 400;
    line-height: 1;
    white-space: nowrap;
  }
  .title-word span { display: inline-block; }
  .title-word--wild { top: 23px; font-size: 116px; }
  .title-word--wild span { transform: scaleX(0.72); }
  .title-word--flower { top: 168px; font-size: 94px; }
  .title-word--flower span { transform: scaleX(0.75); }
  .title-word--honey { top: 572px; font-size: 101px; }
  .title-word--honey span { transform: scaleX(0.85); }
  .brand {
    position: absolute;
    left: 0;
    top: 428px;
    width: 100%;
    display: flex;
    align-items: center;
    justify-content: center;
    gap: 14px;
    font-family: "Archivo", sans-serif;
    font-weight: 800;
    font-size: 34px;
    line-height: 1.2;
  }
  .brand-dot {
    width: 24px;
    height: 24px;
    border-radius: 50%;
    background: var(--ink);
  }
  .tagline {
    position: absolute;
    top: 719px;
    left: 0;
    width: 100%;
    text-align: center;
    font-family: "Archivo", sans-serif;
    font-weight: 800;
    font-size: 32px;
    line-height: 1;
    letter-spacing: 0.5px;
  }
  .state-map {
    position: absolute;
    left: 150px;
    top: 772px;
    width: 287px;
    height: 170px;
    background: linear-gradient(180deg, var(--map-fill), #d9a426);
    border: 3px solid var(--map-edge);
    box-sizing: border-box;
    border-radius: 4px;
  }
  .origin {
    position: absolute;
    left: 105px;
    top: 950px;
    font-family: "Oswald", sans-serif;
    font-weight: 600;
    font-size: 25px;
    line-height: 1;
  }
  .net-weight {
    position: absolute;
    left: 357px;
    top: 988px;
    font-family: "Oswald", sans-serif;
    font-weight: 600;
    font-size: 19px;
    line-height: 1;
  }
</style>
</head>
<body>
  <main class="label">
    <div class="foil-band foil-band--top"></div>

    <h1 class="title-word title-word--wild"><span>WILD</span></h1>
    <p class="title-word title-word--flower"><span>FLOWER</span></p>

    <div class="brand">
      <span class="brand-dot"></span>
      <span class="brand-name">Palmetto Bee Co.</span>
    </div>

    <p class="title-word title-word--honey"><span>HONEY</span></p>
    <p class="tagline">100% PURE &amp; UNFILTERED</p>

    <div class="state-map" role="img" aria-label="Large map of Florida with striped gold fill, marking the honey's origin"></div>

    <p class="origin">PRODUCT OF FLORIDA</p>
    <p class="net-weight">NET WT.</p>

    <div class="foil-band foil-band--bottom"></div>
  </main>
</body>
</html>
```